Paraffin Wax Packaging Design for Nail and Beauty Industry

We need an attractive design for the packaging of our new product, Paraffin Wax. Our company is a wholesale beauty/nail supply company that has been selling to nail salons in the US market for 10 years. We currently sell this product that we buy from another company. Now we want to launch our own brand of Paraffin Wax.

Target Market(s)

Retail nail salons in the US market.

Industry/Entity Type

Industry

Font styles to use
Sans Serif

Colors

Designer to choose colors to be used in the design.

Requirements
Must have
• Our logo (attached).
• All information on the "Ingredient List" (attached).
• Design for Clear Packaging so product can show through.
• Design for Package Dimensions of 4.25" x 11" (110cm x 280 cm).
Nice to have
• Picture related to women's skin and or beauty.
• Contrast as in the design of product that we currently sell (attached).

```html
<!DOCTYPE html>
<html lang="en">
<head>
<meta charset="utf-8">
<title>By Marelle Paraffin Waxes – Pouch Front</title>
<link href="https://fonts.googleapis.com/css2?family=Oswald:wght@400;500;600&display=swap" rel="stylesheet">
<style>
  :root {
    --backdrop: #eeeeee;
    --ink-black: #1b1b1b;
    --wax-red: #e0564f;
    --wax-red-deep: #c9403b;
    --gold: #c9a46a;
    --gold-light: #ecd3a4;
    --lace-brown: #3a2219;
    --text-dark: #2a1512;
    --white: #ffffff;
  }
  * { margin: 0; padding: 0; box-sizing: border-box; }
  html, body { width: 994px; height: 1200px; overflow: hidden; background: var(--backdrop); }
  .canvas { position: relative; width: 994px; height: 1200px; }
  .pouch {
    position: absolute; left: 267px; top: 40px; width: 460px; height: 1120px;
    overflow: hidden; background: var(--wax-red);
    font-family: 'Oswald', sans-serif; color: var(--text-dark);
  }
  .pouch-art { position: absolute; inset: 0; }
  .brand { position: absolute; left: 30px; top: 14px; }
  .brand-name { font-size: 44px; font-weight: 500; color: var(--white); line-height: 1; letter-spacing: 0.5px; }
  .brand-tagline { font-size: 12px; font-weight: 400; color: var(--white); margin-left: 200px; margin-top: 2px; }
  .product-title { position: absolute; left: 52px; top: 418px; font-size: 31px; font-weight: 600; letter-spacing: 0.3px; }
  .claim { position: absolute; left: 52px; font-size: 13.5px; font-weight: 500; line-height: 1.3; text-transform: uppercase; }
  .claim-compat { top: 480px; }
  .claim-moist { top: 532px; }
  .info-head { position: absolute; left: 50px; font-size: 12.5px; font-weight: 500; }
  .info-body { position: absolute; left: 50px; font-size: 9.4px; font-weight: 400; line-height: 1.45; text-transform: uppercase; width: 220px; }
  .ingredients-head { top: 604px; }
  .ingredients-body { top: 624px; }
  .caution-head { top: 728px; }
  .caution-body { top: 748px; }
  .net-weight { position: absolute; left: 48px; top: 808px; font-size: 12px; font-weight: 500; }
</style>
</head>
<body>
<div class="canvas">
  <div class="pouch">
    <svg class="pouch-art" viewBox="0 0 460 1120" width="460" height="1120">
      <defs>
        <linearGradient id="red-field" x1="0" y1="0" x2="0" y2="1">
          <stop offset="0" stop-color="#e4625a"/>
          <stop offset="1" stop-color="#d84a45"/>
        </linearGradient>
        <linearGradient id="gold-band" x1="0" y1="0" x2="1" y2="0">
          <stop offset="0" stop-color="#a8824c"/>
          <stop offset="0.5" stop-color="#f1dbb0"/>
          <stop offset="1" stop-color="#b8915a"/>
        </linearGradient>
        <linearGradient id="photo-tone" x1="1" y1="0" x2="0" y2="1">
          <stop offset="0" stop-color="#e9c2a4"/>
          <stop offset="0.55" stop-color="#d7a585"/>
          <stop offset="1" stop-color="#1b1b1b"/>
        </linearGradient>
        <radialGradient id="hive-tone" cx="0.5" cy="0.5" r="0.6">
          <stop offset="0" stop-color="#f0d7a8"/>
          <stop offset="1" stop-color="#b68b52"/>
        </radialGradient>
      </defs>

      <rect class="red-field" width="460" height="1120" fill="url(#red-field)"/>

      <!-- header band -->
      <polygon class="header-band" points="0,0 460,0 460,72 0,156" fill="var(--ink-black)"/>
      <polygon class="header-gold" points="0,156 460,72 460,112 0,196" fill="url(#gold-band)"/>
      <polygon class="header-gold-edge" points="0,196 460,112 460,120 0,204" fill="#6d4a2a"/>

      <!-- lace ornaments -->
      <path class="lace" role="img" aria-label="Dark brown and gold floral lace ornament"
            d="M0,204 L130,180 C120,240 90,300 50,330 C30,360 20,400 0,430 Z" fill="var(--lace-brown)" opacity="0.85"/>
      <path class="lace" role="img" aria-label="Dark brown and gold floral lace ornament"
            d="M230,150 L460,120 L460,340 C430,320 420,270 380,250 C330,230 280,200 230,150 Z" fill="var(--lace-brown)" opacity="0.85"/>

      <!-- beehive -->
      <ellipse class="beehive" role="img" aria-label="Gold beehive illustration with small bees"
               cx="245" cy="300" rx="68" ry="88" fill="url(#hive-tone)" opacity="0.9"/>

      <!-- lower band with photo -->
      <polygon class="lower-lace" role="img" aria-label="Dark brown and gold floral lace ornament"
               points="0,860 130,820 110,930 0,990" fill="var(--lace-brown)" opacity="0.85"/>
      <polygon class="lower-gold" points="0,980 460,716 460,740 0,1004" fill="url(#gold-band)"/>
      <polygon class="lower-band" points="0,1004 460,740 460,1120 0,1120" fill="var(--ink-black)"/>
      <polygon class="photo" role="img" aria-label="Photo of a woman wrapped in a white towel, sitting and touching her smooth legs"
               points="20,1120 150,1000 300,900 360,760 460,740 460,1120" fill="url(#photo-tone)"/>
    </svg>

    <div class="brand">
      <div class="brand-name">By Marelle</div>
      <div class="brand-tagline">Be Beautiful</div>
    </div>

    <h1 class="product-title">PARAFFIN WAXES</h1>
    <p class="claim claim-compat">Compatible for use with most wax<br>paraffin heat therapy units.</p>
    <p class="claim claim-moist">Deeply moisturizes the skin restoring<br>a healthier look and feel to skin.</p>

    <h2 class="info-head ingredients-head">INGREDIENTS</h2>
    <p class="info-body ingredients-body">Paraffin waxes and hydrocarbon waxes,<br>petrolatum, paraffin oils, apricot kernel<br>oil, fragrance D &amp; C dyes.</p>

    <h2 class="info-head caution-head">CAUTION</h2>
    <p class="info-body caution-body">Paraffin is flammable. Do not use near open<br>flame or an unprotected resistance heater.</p>

    <p class="net-weight">NET WT. 1 LB. (450 G.)</p>
  </div>
</div>
</body>
</html>
```